Letterhead creation for military law attorney

I need letterhead design for my business. We are now only doing military law and need to change address, logo and vision. I like the idea of using an eagle or a jolly roger flag

Target Market(s)

Military Law Clients

Colors
3176b5
85abd2

Requirements
Must have
• We are defending people against the government
Nice to have
• Jolly Roger Flag

```html
<!DOCTYPE html>
<html lang="en">
<head>
<meta charset="utf-8">
<title>Harlan Law, PLLC — Letterhead</title>
<link rel="stylesheet" href="https://fonts.googleapis.com/css2?family=Source+Sans+3:wght@400;700&display=swap">
<style>
  :root {
    --backdrop: #e4e4e4;
    --paper: #f4f4f4;
    --band-blue: #7fa3cc;
    --rule-blue: #3176b5;
    --mark-dark: #3a3a3a;
    --ink: #3b3b3b;
    --ink-soft: #6a6a6a;
    --on-band: #ffffff;
  }
  * { box-sizing: border-box; margin: 0; padding: 0; }
  html, body {
    width: 1200px;
    height: 1200px;
    overflow: hidden;
    background: var(--backdrop);
  }
  .canvas {
    position: relative;
    width: 1200px;
    height: 1200px;
  }
  .letterhead {
    position: absolute;
    left: 197px;
    top: 30px;
    width: 806px;
    height: 1140px;
    background: var(--paper);
    box-shadow: 0 2px 6px rgba(0,0,0,0.12);
    font-family: "Source Sans 3", "Myriad Pro", Arial, sans-serif;
    color: var(--ink);
  }
  .header-band {
    position: absolute;
    left: 0;
    top: 70px;
    width: 100%;
    height: 108px;
    background: var(--band-blue);
  }
  .mark-block {
    position: absolute;
    left: 75px;
    top: 0;
    width: 167px;
    height: 219px;
    background: var(--mark-dark);
  }
  .mark-rule {
    position: absolute;
    left: 75px;
    top: 222px;
    width: 167px;
    height: 4px;
    background: var(--rule-blue);
  }
  .firm-name {
    position: absolute;
    left: 253px;
    top: 70px;
    height: 108px;
    display: flex;
    align-items: center;
    font-size: 28px;
    font-weight: 400;
    letter-spacing: 1px;
    text-transform: uppercase;
    color: var(--on-band);
  }
  .letter-body {
    position: absolute;
    left: 71px;
    top: 292px;
    width: 660px;
    font-size: 18.4px;
    line-height: 23.5px;
  }
  .letter-body p { margin: 0; }
  .letter-body .gap { margin-top: 23.5px; }
  .signature { margin-top: 70px; }
  .footer-contact {
    position: absolute;
    left: 0;
    top: 1104px;
    width: 100%;
    text-align: center;
    font-size: 11px;
    color: var(--ink-soft);
  }
  .footer-contact strong { font-weight: 700; }
  .footer-band {
    position: absolute;
    left: 0;
    bottom: 0;
    width: 100%;
    height: 14px;
    background: var(--band-blue);
  }
</style>
</head>
<body>
<div class="canvas">
  <article class="letterhead">
    <div class="header-band"></div>
    <div class="mark-block"></div>
    <div class="mark-rule"></div>
    <div class="firm-name">Harlan Law, PLLC</div>

    <section class="letter-body">
      <p>Dear Sir,</p>
      <p class="gap">On this good opportunity, I would like to apply as a Instrumentation and Control System Engineer in your company. My name is Dani Marlow, 22 years old, male, single, energetic and healthy. I am a Control System Engineer and graduated from Northfield Technical University (NTU) on May 2007 with GPA 3.78. I would like to have career to expand my experience.</p>
      <p>My personality as a hard worker and fast learner type of person would bring benefit to your company. I will be very appreciated if you could give in opportunity to work in your company.</p>
      <p class="gap">Herewith I enclose my curriculum vitae, which will give details of my qualification.</p>
      <p>I hope my qualifications and experience merit your consideration and look forward to your reply.</p>
      <p class="gap">Sincerely yours,</p>
      <p class="signature">Dani Marlow</p>
      <p>Email : dmarlow@example.com</p>
    </section>

    <footer class="footer-contact">
      <strong>PO BOX</strong> 219 Fairview, TN 37062 &nbsp;-&nbsp; <strong>Phone</strong> (555) 014 - 2280 &nbsp;-&nbsp; <strong>FAX</strong> (555) 014 - 2281
    </footer>
    <div class="footer-band"></div>
  </article>
</div>
</body>
</html>
```